zipbeatz.net website for a mobile DJ entertainment company

I am looking for a business card design for a mobile DJ company. We perform all types of events from weddings to kids parties and I would like a card to be fun, bright, energetic and give the impression of a great time. I am also attempting to creating a visual brand and recognition by leveraging a custom vinyl wrap that I am using for my vehicle and trailer using paint splatter. I would like the design on the front to look like multi-color paint splatter across the card with the company website "ZIPBEATZ.net" prominently displayed and my contact information on the back. The back can be more plain then the front with just contact information with maybe a muted version of the front as a background.

Contact Information for Business Card

See above

Font styles to use
Serif

Colors
9bcb3b
0293ce
ec1f27
fbed22
6b449b
f78f20

Requirements
Nice to have
• Would like ti close enough to my truck to be recognized as one product.

```html
<!DOCTYPE html>
<html lang="en">
<head>
<meta charset="utf-8">
<title>ZIPBEATZ.net Business Card</title>
<link href="https://fonts.googleapis.com/css2?family=Oswald:wght@500;600&family=Work+Sans:wght@400;500&display=swap" rel="stylesheet">
<style>
  :root {
    --backdrop: #161616;
    --backdrop-light: #2a2a2a;
    --card: #1e1e1e;
    --card-sheen: #2b2b2b;
    --brand-purple: #6b449b;
    --brand-purple-bright: #7a52b3;
    --brand-green: #9bcb3b;
    --brand-blue: #0293ce;
    --brand-red: #ec1f27;
    --brand-yellow: #fbed22;
    --brand-orange: #f78f20;
    --ink-light: #f2f2f2;
    --ink-soft: #d8d8d8;
  }
  * { box-sizing: border-box; margin: 0; padding: 0; }
  html, body { width: 1200px; height: 900px; overflow: hidden; }
  body {
    background: radial-gradient(ellipse at 50% 40%, var(--backdrop-light), var(--backdrop) 75%);
    font-family: "Work Sans", sans-serif;
    position: relative;
  }
  .card {
    position: absolute;
    left: 250px;
    width: 700px;
    height: 400px;
    overflow: hidden;
    background: linear-gradient(120deg, var(--card) 0%, var(--card) 55%, var(--card-sheen) 100%);
    box-shadow: 0 18px 40px rgba(0,0,0,0.6);
  }
  .card-front { top: 30px; display: flex; align-items: center; justify-content: center; }
  .card-back { top: 470px; }

  .splatter-field {
    position: absolute;
    inset: 0;
    background:
      radial-gradient(circle at 12% 22%, var(--brand-red) 0, transparent 22%),
      radial-gradient(circle at 30% 80%, var(--brand-yellow) 0, transparent 20%),
      radial-gradient(circle at 55% 12%, var(--brand-blue) 0, transparent 22%),
      radial-gradient(circle at 78% 70%, var(--brand-green) 0, transparent 24%),
      radial-gradient(circle at 92% 18%, var(--brand-orange) 0, transparent 20%),
      radial-gradient(circle at 45% 60%, var(--brand-purple) 0, transparent 26%);
  }
  .card-front .splatter-field { opacity: 0.55; }
  .card-back .splatter-field { opacity: 0.14; }

  .front-url {
    position: relative;
    font-family: "Oswald", sans-serif;
    font-weight: 600;
    font-size: 44px;
    letter-spacing: 7px;
    color: var(--ink-light);
    padding: 10px 26px;
    background: rgba(20,20,20,0.82);
  }

  .identity {
    position: absolute;
    top: 140px;
    right: 400px;
    text-align: right;
  }
  .person-name {
    font-family: "Oswald", sans-serif;
    font-weight: 600;
    font-size: 38px;
    line-height: 1;
    color: var(--brand-purple-bright);
    letter-spacing: -0.5px;
  }
  .person-role {
    margin-top: 8px;
    font-size: 18px;
    letter-spacing: 2px;
    color: var(--ink-soft);
  }
  .divider {
    position: absolute;
    left: 318px;
    top: 140px;
    width: 2px;
    height: 72px;
    background: var(--ink-light);
  }
  .contact-list {
    position: absolute;
    left: 342px;
    top: 142px;
    list-style: none;
  }
  .contact-item {
    display: flex;
    align-items: center;
    gap: 14px;
    height: 24px;
    font-size: 18px;
    letter-spacing: 1.6px;
    color: var(--ink-light);
  }
  .contact-icon { width: 13px; height: 13px; flex: none; }
  .accent { color: var(--brand-purple-bright); }
  .address {
    position: absolute;
    left: 70px;
    bottom: 78px;
    font-size: 18px;
    letter-spacing: 2px;
    color: var(--ink-light);
  }
</style>
</head>
<body>
  <section class="card card-front">
    <div class="splatter-field" role="img" aria-label="Multicolour paint splatter in red, yellow, blue, green, orange and purple"></div>
    <p class="front-url">WWW.ZIPBEATZ.NET</p>
  </section>

  <section class="card card-back">
    <div class="splatter-field" role="img" aria-label="Muted multicolour paint splatter background"></div>
    <div class="identity">
      <h1 class="person-name">DANIEL REYES</h1>
      <p class="person-role">Director</p>
    </div>
    <div class="divider"></div>
    <ul class="contact-list">
      <li class="contact-item">
        <svg class="contact-icon" viewBox="0 0 16 16" fill="none" stroke="#7a52b3" stroke-width="1.6"><path d="M3 1.5h3l1.2 3.2-1.8 1.2a8 8 0 0 0 4.7 4.7l1.2-1.8 3.2 1.2v3c0 .6-.5 1-1 1A13 13 0 0 1 2 2.5c0-.5.4-1 1-1z"/></svg>
        <span>+330 5550-1427</span>
      </li>
      <li class="contact-item">
        <svg class="contact-icon" viewBox="0 0 16 16" fill="none" stroke="#7a52b3" stroke-width="1.4"><rect x="1" y="3" width="14" height="10" rx="1"/><path d="M1 3.5l7 5.5 7-5.5"/></svg>
        <span>info@ZIPBEATZ.net</span>
      </li>
      <li class="contact-item">
        <svg class="contact-icon" viewBox="0 0 16 16" fill="none" stroke="#7a52b3" stroke-width="1.2"><circle cx="8" cy="8" r="6.5"/><ellipse cx="8" cy="8" rx="3" ry="6.5"/><path d="M1.5 8h13M2.5 4.8h11M2.5 11.2h11"/></svg>
        <span>www.<span class="accent">ZIPBEATZ</span>.net</span>
      </li>
    </ul>
    <p class="address">1820 Harbor Lane New York, NY 10052</p>
  </section>
</body>
</html>
```